"Giggle Garden Days" Summer Camp flyer for preschool

I need a flyer for our preschool's summer camp. Our summer theme is GIGGLE garden DAYS. the theme MUST be displayed. We would like a mad scientist with crazy hair look with test tubes and goggles PROMINENTLY DISPLAYED on the flyer. this is for a preschool so we don't want the scientist to look scary. Our logo needs to be included on the flyer. The age range for the school is 6weeks to 6 years (you can add "6 weeks to 6 years" somewhere small on the flyer). Please add "Camp starts June 5th" and Sign up for 1 camp or all!". The weekly themes for the camp are ...
Journey into Outer Space
Rock Out in Geology
Weather
Water Extravagnaza
Biology
Physics - Force & Motion
Light
Sensational Sounds
Budding Builders
Krazy Kitchen Chemistry
Electromagnetism
It's Hip to Be Healthy
we don't want these on the flyer but maybe you can use them for image inspiration.
Attached is our logo and some verbiage that can be used.

moms and dads of preschool age kids

Preschool

• our logo, title of the camp, dates, a Mad Scientist with crazy hair, test tube, and goggles. attached is image of scientist. i will purchase this once art is approved.
• it would be nice to have the weekly themes on the flyer

```html
<!DOCTYPE html>
<html lang="en">
<head>
<meta charset="utf-8">
<title>Giggle Garden Days – Summer Camp Flyer</title>
<link rel="stylesheet" href="https://fonts.googleapis.com/css2?family=Bebas+Neue&family=Open+Sans:wght@700&family=Noto+Serif:wght@700&display=swap">
<style>
  :root {
    --page: #e8e3da;
    --cream: #efefca;
    --white: #ffffff;
    --brown: #5a4141;
    --ink: #4b3434;
    --bullet: #e4e4b6;
    --photo-light: #e9edf2;
    --photo-mid: #b9a6d6;
    --photo-deep: #7a5fb0;
    --badge: #3c8d9a;
  }
  html, body {
    margin: 0;
    width: 1200px;
    height: 800px;
    overflow: hidden;
    background: var(--page);
  }
  .flyer {
    position: absolute;
    left: 305px;
    top: 20px;
    width: 659px;
    height: 850px;
    transform: scale(0.894);
    transform-origin: top left;
    background: var(--cream);
    overflow: hidden;
    box-shadow: 0 6px 18px rgba(0,0,0,0.18);
  }
  .flyer-shapes {
    position: absolute;
    inset: 0;
  }
  .title {
    position: absolute;
    left: 24px;
    top: 22px;
    margin: 0;
    font-family: "Bebas Neue", sans-serif;
    font-weight: 400;
    font-size: 78px;
    line-height: 70px;
    color: var(--ink);
    letter-spacing: 0.5px;
  }
  .start-date {
    position: absolute;
    left: 51px;
    top: 252px;
    margin: 0;
    font-family: "Bebas Neue", sans-serif;
    font-weight: 400;
    font-size: 44px;
    line-height: 44px;
    color: var(--ink);
  }
  .sign-up {
    position: absolute;
    left: 79px;
    top: 294px;
    margin: 0;
    font-family: "Noto Serif", serif;
    font-weight: 700;
    font-size: 18px;
    color: var(--ink);
  }
  .themes-heading {
    position: absolute;
    left: 45px;
    top: 419px;
    margin: 0;
    font-family: "Bebas Neue", sans-serif;
    font-weight: 400;
    font-size: 29px;
    color: var(--ink);
  }
  .theme-list {
    position: absolute;
    top: 457px;
    margin: 0;
    padding: 0;
    list-style: none;
    font-family: "Open Sans", sans-serif;
    font-weight: 700;
    font-size: 20.5px;
    line-height: 26px;
    color: var(--ink);
  }
  .theme-list li {
    position: relative;
    padding-left: 19px;
    white-space: nowrap;
  }
  .theme-list li::before {
    content: "";
    position: absolute;
    left: 0;
    top: 9px;
    width: 9px;
    height: 9px;
    border-radius: 50%;
    background: var(--bullet);
  }
  .theme-list--left { left: 28px; }
  .theme-list--right { left: 355px; }
  .contact {
    position: absolute;
    left: 60px;
    width: 530px;
    top: 789px;
    margin: 0;
    text-align: center;
    font-family: "Noto Serif", serif;
    font-weight: 700;
    font-size: 18.5px;
    line-height: 23px;
    color: var(--ink);
  }
  .contact .divider { font-weight: 400; padding: 0 3px; }
  .school-mark {
    position: absolute;
    left: 578px;
    top: 768px;
    width: 70px;
    text-align: center;
  }
  .school-mark-dot {
    display: block;
    width: 38px;
    height: 38px;
    margin: 0 auto 4px;
    border-radius: 50%;
    background: var(--badge);
  }
  .school-mark-name {
    font-family: "Open Sans", sans-serif;
    font-weight: 700;
    font-size: 11px;
    line-height: 12px;
    color: var(--ink);
  }
</style>
</head>
<body>
  <main class="flyer">
    <svg class="flyer-shapes" viewBox="0 0 659 850" width="659" height="850" aria-hidden="false">
      <defs>
        <linearGradient id="scientistTones" x1="0" y1="0" x2="1" y2="1">
          <stop offset="0" stop-color="var(--photo-light)"/>
          <stop offset="0.45" stop-color="var(--photo-mid)"/>
          <stop offset="1" stop-color="var(--photo-light)"/>
        </linearGradient>
      </defs>
      <path class="white-field" fill="var(--white)"
        d="M0,372 C120,392 290,380 420,328 C520,290 600,262 659,250 L659,686 C560,738 430,770 330,770 C200,770 70,735 0,692 Z"/>
      <path class="scientist-photo" fill="url(#scientistTones)" role="img"
        aria-label="Photo of a friendly scientist in goggles and purple gloves holding up a bottle and a flask"
        d="M330,18 L659,18 L659,268 C540,225 430,203 330,196 Z"/>
      <path class="accent-band" fill="var(--brown)"
        d="M0,228 C160,193 420,183 659,262 L659,283 C420,205 170,212 0,246 Z"/>
    </svg>

    <h1 class="title">GIGGLE garden<br>DAYS</h1>

    <p class="start-date">CAMP STARTS JUNE 5TH</p>
    <p class="sign-up">Sign up for 1 camp or all!</p>

    <h2 class="themes-heading">WEEKLY THEMES:</h2>
    <ul class="theme-list theme-list--left">
      <li>Journey into Outer Space</li>
      <li>Rock Out in Geology</li>
      <li>Weather</li>
      <li>Water Extravagnaza</li>
      <li>Biology</li>
      <li>Physics - Force &amp; Motion</li>
    </ul>
    <ul class="theme-list theme-list--right">
      <li>Light</li>
      <li>Sensational Sounds</li>
      <li>Budding Builders</li>
      <li>Krazy Kitchen Chemistry</li>
      <li>Electromagnetism</li>
      <li>It's Hip to Be Healthy</li>
    </ul>

    <p class="contact">www.sunnyburrow.com <span class="divider">|</span> info@sunnyburrow.com<br>555.010.2468</p>

    <div class="school-mark">
      <span class="school-mark-dot"></span>
      <span class="school-mark-name">Sunny Burrow</span>
    </div>
  </main>
</body>
</html>
```